Kinderbuchverlag sucht Buch-/E-Book-Cover
Zielgruppe
Wir sind ein Kinderbuchverlag. Unsere Zielgruppe sind Kinder, bei diesem Buch im Alter von 3 bis 10 Jahren.
Aufgabenstellung
Das Cover benötige ich für E-book, Taschenbuch und Hardcover Version. Das Cover soll modern passend für Kinder gestalten sein, aber auch Eltern ansprechen. Das Cover soll nach einem hochwertigen Verlags-Cover aussehen und nicht nach einem billigen Publishing Buch. Benutzen Sie moderne Schriften passend für Kinder.
Format:
Print & Hardcover: 13,97 x 21,59 cm (5,5' x 8,5')
Seiten: 76
für Borvell Lesepad
Bitte unser Verlagslogo unten links auf die vordere Seite (Front) mit einfügen.
Buchtitel: Als das Mondlicht im Schneegarten flüstert
Untertitel: Verträumte Erzählungen über flinke Kobolde (Kinderbuch über das Rätsel der Kobolde und ihrer Laternen)
Autor: Henrike L. Bosshammer
Text für die Rückseite des Covers muss drauf:
Ein zauberhafter Blick hinter die Wichteltüren
Ein kräftiges Schneegestöber, ein allzu neugieriger Dackelwelpe und dann auch noch ein Stuhl, der sich einfach nicht reparieren lassen will: Die Weihnachtszeit bei den Menschen stellt die Wichtel vor so manche Herausforderung. Da wird jeder einzelne Tag für Fridolin, Gottfried, Jonte, Paule und ihre Freunde zu einem echten Abenteuer. In sechs spannenden und lustigen Geschichten nimmt dieses Wichtel-Buch die Kinder mit auf eine zauberhafte Reise in die Welt der Wichtel.
Denn diese liebenswerten Gesellen beziehen jedes Jahr - pünktlich zum 1. Dezember - ihre Wohnungen bei den Menschen, stets gut erkennbar an den kleinen Wichteltüren. Bis zum Heiligen Abend begleiten sie 'ihre' Familien, stehen ihnen still und heimlich zur Seite und haben dabei stets nur eines im Sinn: wunderbaren Weihnachtszauber zu verbreiten.
• Dieses Büchlein mit farbigen Illustrationen ist für Kinder von zwei bis acht Jahren geschrieben.
• Diese unterhaltsamen Geschichten eignen sich hervorragend zum Vorlesen, Schulkinder können sich jedoch auch selbst schon daran versuchen.
• Dieses Buch lädt Kinder ein, die Welt..

```html
<!DOCTYPE html>
<html lang="de">
<head>
<meta charset="utf-8">
<title>Als das Mondlicht im Schneegarten flüstert – Umschlag</title>
<link href="https://fonts.googleapis.com/css2?family=Amatic+SC:wght@400;700&family=Roboto:wght@400;700&family=Roboto+Condensed:wght@400&display=swap" rel="stylesheet">
<style>
  :root{
    --wall-dark:#7a1616;
    --wall-mid:#a83a35;
    --wall-light:#b4504a;
    --skirting:#eccfd0;
    --floor:#d7844e;
    --floor-dark:#c46c3a;
    --banner:#4f9a3c;
    --white:#ffffff;
    --door:#2aa3c7;
    --gnome:#d8322a;
    --ink:#2a2a2a;
  }
  html,body{margin:0;padding:0;overflow:hidden;}
  body{width:1200px;height:895px;}
  .cover{
    position:relative;width:1200px;height:895px;overflow:hidden;
    background:radial-gradient(ellipse at 30% 40%, var(--wall-light) 0%, var(--wall-mid) 40%, var(--wall-dark) 100%);
    color:var(--white);font-family:"Roboto",sans-serif;
  }
  .skirting{position:absolute;left:0;right:0;top:667px;height:88px;
    background:linear-gradient(180deg,#f3dcdc 0%,var(--skirting) 60%,#d9b0b0 100%);}
  .floor{position:absolute;left:0;right:0;top:755px;bottom:0;
    background:linear-gradient(180deg,var(--floor-dark) 0%,var(--floor) 40%,#e0955f 100%);}

  /* back */
  .back{position:absolute;left:37px;top:50px;width:506px;}
  .back-heading{font-family:"Amatic SC",sans-serif;font-weight:700;font-size:34px;
    margin:0 0 4px;line-height:1;white-space:nowrap;}
  .back p{font-size:13.4px;line-height:20.5px;margin:0 0 20.5px;text-align:justify;hyphens:auto;}
  .back ul{margin:0 0 20.5px;padding:0 0 0 12px;font-size:13.4px;line-height:20.5px;width:480px;}
  .back li{margin:0;list-style:"•  ";}

  /* spine */
  .spine{position:absolute;left:586px;top:0;width:30px;height:895px;}
  .spine-title,.spine-author{position:absolute;left:50%;white-space:nowrap;line-height:1;
    transform:translate(-50%,-50%) rotate(-90deg);}
  .spine-title{top:237px;font-family:"Amatic SC",sans-serif;font-weight:700;font-size:27px;letter-spacing:1.5px;}
  .spine-author{top:567px;font-family:"Roboto Condensed",sans-serif;font-size:18px;}

  /* front */
  .front{position:absolute;left:646px;top:0;width:554px;height:895px;}
  .author{position:absolute;left:0;right:0;top:27px;text-align:center;line-height:1;
    font-family:"Roboto Condensed",sans-serif;font-size:29px;}
  .title{margin:0;font-family:"Amatic SC",sans-serif;font-weight:700;}
  .title span{position:absolute;left:0;right:0;text-align:center;line-height:1;white-space:nowrap;}
  .title .t-small{top:72px;font-size:44px;}
  .title .t-huge{top:84px;font-size:150px;letter-spacing:2px;}
  .title .t-row{top:212px;font-size:80px;}
  .title .t-row small{font-size:38px;}
  .banner{position:absolute;left:56px;top:297px;width:380px;height:88px;
    background:var(--banner);border:2px solid #e9f3e3;border-radius:14px 6px 22px 8px;
    display:flex;align-items:center;justify-content:center;text-align:center;
    font-family:"Amatic SC",sans-serif;font-weight:700;font-size:21px;line-height:24px;padding:0 14px;box-sizing:border-box;}
  .scene{position:absolute;left:56px;top:398px;width:426px;height:437px;border-radius:48% 48% 8px 8px / 30% 30% 8px 8px;
    background:linear-gradient(120deg,var(--door) 0%,#2b8fb0 45%,var(--gnome) 80%,#b82720 100%);opacity:.9;}
  .publisher{position:absolute;left:0;top:836px;display:flex;align-items:center;gap:8px;}
  .publisher .mark{width:20px;height:20px;border-radius:50%;background:var(--ink);}
  .publisher .name{font-family:"Roboto",sans-serif;font-weight:700;font-size:21px;line-height:20px;color:var(--ink);letter-spacing:1px;}
</style>
</head>
<body>
<div class="cover">
  <div class="skirting"></div>
  <div class="floor"></div>

  <section class="back">
    <h2 class="back-heading">Ein zauberhafter Blick hinter die Wichteltüren</h2>
    <p>Ein kräftiges Schneegestöber, ein allzu neugieriger Dackelwelpe und dann auch noch ein Stuhl, der sich einfach nicht reparieren lassen will: Die Weihnachtszeit bei den Menschen stellt die Wichtel vor so manche Herausforderung. Da wird jeder einzelne Tag für Fridolin, Gottfried, Jonte, Paule und ihre Freunde zu einem echten Abenteuer. In sechs spannenden und lustigen Geschichten nimmt dieses Wichtel-Buch die Kinder mit auf eine zauberhafte Reise in die Welt der Wichtel.</p>
    <p>Denn diese liebenswerten Gesellen beziehen jedes Jahr - pünktlich zum 1. Dezember - ihre Wohnungen bei den Menschen, stets gut erkennbar an den kleinen Wichteltüren. Bis zum Heiligen Abend begleiten sie ‚ihre‘ Familien, stehen ihnen still und heimlich zur Seite und haben dabei stets nur eines im Sinn: wunderbaren Weihnachtszauber zu verbreiten.</p>
    <ul>
      <li>Dieses Büchlein mit farbigen Illustrationen ist für Kinder von zwei bis acht Jahren geschrieben.</li>
      <li>Diese unterhaltsamen Geschichten eignen sich hervorragend zum Vorlesen, Schulkinder können sich jedoch auch selbst schon daran versuchen.</li>
      <li>Dieses Buch lädt Kinder ein, die Welt der Wichtel kennenzulernen und verkürzt auf magische Weise die Zeit bis zum Weihnachtsabend</li>
    </ul>
    <p>Die Tradition der Wichteltüren stammt ursprünglich aus Skandinavien, insbesondere in Dänemark ist sie weit verbreitet. Doch auch hierzulande sind immer mehr Menschen von der Magie dieser winzigen Türen fasziniert. Ein Blick dahinter ist den Menschen normalerweise strengstens untersagt. Für die Leser dieses Büchleins jedoch öffnen sich die Wichteltüren einen Spalt breit und gewähren Einblicke in die wundersame Welt dieser liebenswerten Wesen. Es wird spannend und heiter, kurzum: einfach wichtelmäßig magisch ...</p>
  </section>

  <aside class="spine">
    <div class="spine-title">Als das Mondlicht im Schneegarten flüstert</div>
    <div class="spine-author">Henrike L. Bosshammer</div>
  </aside>

  <section class="front">
    <div class="author">Henrike L. Bosshammer</div>
    <h1 class="title">
      <span class="t-small">Als das</span>
      <span class="t-huge">Mondlicht</span>
      <span class="t-row"><small>im</small> Schneegarten <small>flüstert</small></span>
    </h1>
    <div class="banner">Verträumte Erzählungen über flinke Kobolde (Kinderbuch über das Rätsel der Kobolde und ihrer Laternen)</div>
    <div class="scene" role="img" aria-label="Illustration: kleine blaue Tür mit Leiter und Briefkasten an der Wand, davor ein fröhlicher Kobold mit roter Mütze"></div>
    <div class="publisher">
      <span class="mark"></span>
      <span class="name">KLEEBLATT<br>VERLAG</span>
    </div>
  </section>
</div>
</body>
</html>
```